Web Site

Target Market(s)

CEOs and International Sales & Marketing Directors of International Companies who wish to expand their business reach to Dubai and the Middle East and are looking for a local professional partner to work with.

Requirements
Must have
• Creativity is key. We don't want the normal standard boxes of text and boxes of pics. Be as creative as you like.
Nice to have
• (This is only a suggestion, we welcome your creativity)
- The center of all pages could be large rotating pictures which display professional corporate men/women working in an office, images of Dubai, the UAE, skyscrapers of business towers in Dubai, ..etc.
- Images should reflect Dubai and the Arab World as a modern, fast-paced, growing modern market - Not Traditional)
Should not have
• Not so colorful, the fewer colors you use, the better.
Not Crammed or Busy
Not Traditional but modern

```html
<!DOCTYPE html>
<html lang="en">
<head>
<meta charset="utf-8">
<title>Cedar Group</title>
<link rel="stylesheet" href="https://fonts.googleapis.com/css2?family=Open+Sans:wght@400;600&family=Arimo:wght@400;700&display=swap">
<style>
:root{
  --ink:#2b2b2b;
  --text:#3a3a3a;
  --muted:#8a8a8a;
  --accent:#8c1d14;
  --accent-tab:#a8392a;
  --rule:#d9d9d9;
  --nav-top:#f4f4f4;
  --nav-bottom:#dedede;
  --white:#ffffff;
}
*{box-sizing:border-box;margin:0;padding:0}
html,body{width:1200px;height:986px;overflow:hidden;background:var(--white)}
body{position:relative;font-family:"Arimo",Arial,sans-serif;color:var(--text)}
a{text-decoration:none;color:inherit}

.site-header{position:absolute;left:0;top:0;width:1200px;height:135px;
  background:linear-gradient(#fafbfc,#ffffff)}
.brand{position:absolute;left:0;width:1200px;top:48px;text-align:center;
  font-family:"Open Sans",sans-serif;font-weight:600;font-size:30px;letter-spacing:3px;color:var(--ink)}
.brand-mark{display:inline-block;width:14px;height:14px;background:var(--accent);margin-right:10px;vertical-align:2px}
.utility-links{position:absolute;right:51px;top:18px;font-size:12px;color:var(--muted)}
.utility-links a{margin:0 5px}
.utility-links .sep{color:#bbb}
.utility-links .current{color:var(--accent)}

.main-nav{position:absolute;left:0;top:135px;width:1200px;height:42px;
  background:linear-gradient(var(--nav-top),var(--nav-bottom));border-bottom:4px solid var(--accent)}
.main-nav a{position:absolute;top:0;height:38px;line-height:38px;
  font-family:"Open Sans",sans-serif;font-size:15px;color:#555}
.main-nav .active{background:var(--accent-tab);color:var(--white);padding:0 17px}

.hero{position:absolute;left:0;top:177px;width:1200px;height:358px;overflow:hidden}
.hero-photo{position:absolute;inset:0;
  background:linear-gradient(180deg,#7c8ca6 0%,#a3a2a6 35%,#77736e 70%,#8e8983 100%)}
.hero-caption{position:absolute;left:57px;top:104px;width:517px;height:237px;
  background:rgba(40,44,50,.55);padding:20px 0 0 24px}
.hero-caption h1{font-family:"Open Sans",sans-serif;font-weight:400;font-size:25px;color:var(--white);margin-bottom:6px}
.hero-caption p{font-size:14.5px;line-height:17px;color:#eee;width:468px}
.read-more{position:absolute;left:24px;top:133px;width:94px;height:24px;background:var(--accent);
  color:var(--white);font-size:12.5px;line-height:24px;padding-left:10px}
.read-more svg{position:absolute;right:8px;top:8px}
.slide-dots{position:absolute;left:26px;top:202px;display:flex;gap:14px}
.slide-dots span{width:11px;height:11px;border-radius:50%;background:rgba(255,255,255,.45)}
.slide-dots .on{background:var(--white)}

.info-column{position:absolute;top:563px;width:336px}
.info-column h2{font-family:"Open Sans",sans-serif;font-weight:400;font-size:19.5px;color:#222;
  padding-bottom:6px;border-bottom:2px solid var(--rule);margin-bottom:13px}
.info-column p{font-size:14px;line-height:17px}
.link-list{list-style:none;margin-top:12px}
.link-list li{position:relative;padding-left:21px;height:26px;font-size:14px;color:var(--accent);line-height:17px}
.link-list li::before{content:"";position:absolute;left:2px;top:4px;border-left:6px solid #555;
  border-top:4px solid transparent;border-bottom:4px solid transparent}
.info-column h3{font-family:"Open Sans",sans-serif;font-weight:400;font-size:15.5px;color:var(--accent);margin-bottom:2px}
.info-column .block{margin-bottom:12px}

.site-footer{position:absolute;left:0;top:810px;width:1200px;height:176px}
.footer-band{position:absolute;left:57px;top:0;width:1092px;height:40px;
  background:linear-gradient(90deg,#fff,#eee 20%,#eee 80%,#fff);
  -webkit-mask:linear-gradient(#000,transparent);mask:linear-gradient(#000,transparent)}
.social-links{position:absolute;left:0;width:1200px;top:40px;text-align:center;
  font-family:"Open Sans",sans-serif;font-weight:600;font-size:18px;color:#9a9a9a}
.social-links a{margin:0 12px}
.contact-line{position:absolute;left:0;width:1200px;top:81px;text-align:center;font-size:12.5px;color:#333}
.contact-line .mail{color:var(--accent)}
.copyright{position:absolute;left:0;width:1200px;top:101px;text-align:center;font-size:12.5px;color:#333}
</style>
</head>
<body>
<header class="site-header">
  <div class="brand"><span class="brand-mark"></span>CEDAR GROUP</div>
  <nav class="utility-links">
    <a href="#">Login</a><span class="sep">|</span><a href="#" class="current">Carrers</a><span class="sep">|</span><a href="#">Sitemap</a><span class="sep">|</span><a href="#">Help</a>
  </nav>
</header>

<nav class="main-nav">
  <a href="#" class="active" style="left:57px">Home</a>
  <a href="#" style="left:168px">About the Group</a>
  <a href="#" style="left:328px">Chairman’s Message</a>
  <a href="#" style="left:514px">Divisions</a>
  <a href="#" style="left:644px">Group Companies</a>
  <a href="#" style="left:821px">Employment &amp; Association</a>
  <a href="#" style="left:1049px">Contact us</a>
</nav>

<section class="hero">
  <div class="hero-photo" role="img" aria-label="Photo of Dubai business towers with a portrait of a businessman on the right"></div>
  <div class="hero-caption">
    <h1>Cedar Business Services</h1>
    <p>Cedar Business Services is an experienced company with a regional focus while maintaining a global representation. Our spectrum of services covers all aspects of doing business in the UAE.</p>
    <a href="#" class="read-more">Readmore<svg width="6" height="8" viewBox="0 0 6 8"><path d="M0 0L6 4L0 8Z" fill="#e08a7a"/></svg></a>
    <div class="slide-dots"><span class="on"></span><span></span><span></span><span></span></div>
  </div>
</section>

<section class="info-column" style="left:57px">
  <h2>Chairman’s Message</h2>
  <p>CEDARGROUP was founded at the time the United Arab Emirates became an independent nation. From modest beginnings, the group has matched the pace of growth of Dubai.</p>
  <ul class="link-list">
    <li>Read more messages</li>
    <li>View chairman’s profile</li>
  </ul>
</section>

<section class="info-column" style="left:434px">
  <h2>Services</h2>
  <ul class="link-list" style="margin-top:0">
    <li>Legal Services</li>
    <li>Media Production</li>
    <li>Real Estate Investment &amp; Management</li>
    <li>General Trading</li>
    <li>Business Services</li>
    <li>Telecommunication Products &amp;Services</li>
  </ul>
</section>

<section class="info-column" style="left:813px">
  <h2>Employment &amp; Alliances</h2>
  <div class="block">
    <h3>Employment</h3>
    <p>For Employment opportunities with us, please contact us on info@cedar-grp.com.</p>
  </div>
  <div class="block">
    <h3>Alliances</h3>
    <p>For Strategic Association opportunities with us, please contact us on info@cedar-grp.com.</p>
  </div>
</section>

<footer class="site-footer">
  <div class="footer-band"></div>
  <nav class="social-links"><a href="#">Updates</a><a href="#">Videos</a><a href="#">Community</a></nav>
  <p class="contact-line">+971 4 210 4480 &nbsp;|&nbsp; <span class="mail">info@cedar-grp.com</span></p>
  <p class="copyright">© 2012 CEDAR Group. All rights reserved. Legal Privacy</p>
</footer>
</body>
</html>
```